Facebook Header Design Project.

I'm supplying white and colored logos. The Facebook page already exists. URL = https://www.examplesocial.test/lumacrest.design The design should not be based on what's already there. Consider mobile implications of the design. This Design will form the designs of other social media headers. LumaCrest is a web design | digital marketing company.

Target Market(s)

People interested in web design | digital marketing services.

Industry/Entity Type

LumaCrest is a web design | digital marketing company. That should be clear in the design.

Colors
0054AA
0677BA
7BADD7
CADEEF
E8F1F8

Requirements
Must have
• Logo. Use Facebook header image dimension.
Nice to have
• Use a color scheme like the logo and feel free to add a color or two from the other side of the color whee.

```html
<!DOCTYPE html>
<html lang="en">
<head>
<meta charset="utf-8">
<title>LumaCrest – Facebook Cover</title>
<link href="https://fonts.googleapis.com/css2?family=Montserrat:wght@300;400;700;800&display=swap" rel="stylesheet">
<style>
  :root {
    --brand-deep: #0f3f93;
    --brand-blue: #0054aa;
    --brand-mid: #0677ba;
    --brand-soft: #7badd7;
    --brand-pale: #cadeef;
    --brand-mist: #e8f1f8;
    --ink: #1d3f8f;
    --stage: #5a5a5a;
    --cover-light: #ffffff;
    --cover-grey: #e4e4e6;
  }
  * { box-sizing: border-box; margin: 0; padding: 0; }
  html, body {
    width: 1200px; height: 1200px; overflow: hidden;
  }
  body {
    background: var(--stage);
    font-family: "Montserrat", sans-serif;
    position: relative;
  }
  .cover {
    position: absolute;
    left: 40px; top: 387px;
    width: 1120px; height: 425px;
    background:
      radial-gradient(ellipse at 70% 45%, #d9d9dc 0%, rgba(217,217,220,0) 60%),
      linear-gradient(100deg, var(--cover-light) 0%, #f4f4f5 45%, var(--cover-grey) 100%);
    border-bottom: 4px solid var(--brand-blue);
    overflow: hidden;
  }
  .brand {
    position: absolute;
    left: 72px; top: 58px;
    display: flex; align-items: center; gap: 14px;
  }
  .brand__dot {
    width: 38px; height: 38px; border-radius: 50%;
    background: var(--brand-mid);
  }
  .brand__name {
    font-weight: 800;
    font-size: 56px;
    color: var(--brand-blue);
    letter-spacing: -1px;
    line-height: 1;
  }
  .headline {
    position: absolute;
    left: 65px; top: 160px;
    color: var(--ink);
    line-height: 1;
  }
  .headline__light {
    display: block;
    font-weight: 300;
    font-size: 46px;
    letter-spacing: 1px;
    padding-left: 1px;
  }
  .headline__band {
    display: inline-block;
    background: var(--brand-deep);
    color: #ffffff;
    font-weight: 800;
    font-size: 42px;
    padding: 4px 12px 3px 2px;
    margin-top: 6px;
    letter-spacing: 0.5px;
  }
  .headline__band .amp { font-weight: 300; }
  .headline__band--one { margin-top: 8px; }
  .headline__band--two { margin-top: 9px; }
  .headline__light--end { margin-top: 4px; }
  .site-url {
    position: absolute;
    left: 800px; top: 58px;
    font-size: 17px;
    letter-spacing: 3px;
    color: var(--ink);
    font-weight: 400;
  }
  .site-url b { font-weight: 700; }
  .illustration {
    position: absolute;
    left: 543px; top: 110px;
    width: 536px; height: 270px;
    border-radius: 14px;
    background:
      radial-gradient(circle at 22% 55%, rgba(226,76,86,0.55) 0%, rgba(226,76,86,0) 30%),
      radial-gradient(circle at 62% 55%, rgba(122,88,200,0.55) 0%, rgba(122,88,200,0) 38%),
      radial-gradient(circle at 88% 40%, rgba(240,170,190,0.55) 0%, rgba(240,170,190,0) 30%),
      linear-gradient(120deg, rgba(202,222,239,0.5), rgba(190,170,230,0.45));
  }
</style>
</head>
<body>
  <section class="cover">
    <div class="brand">
      <span class="brand__dot"></span>
      <span class="brand__name">LumaCrest</span>
    </div>

    <p class="site-url">www.<b>lumacrest</b>.test</p>

    <h1 class="headline">
      <span class="headline__light">WE ARE A</span>
      <span class="headline__band headline__band--one">WEB DESIGN <span class="amp">&amp;</span></span><br>
      <span class="headline__band headline__band--two">DIGITAL MARKETING</span>
      <span class="headline__light headline__light--end">COMPANY.</span>
    </h1>

    <div class="illustration" role="img" aria-label="Illustration of a smartphone with a megaphone, a design book, a desktop monitor showing a web layout, a light bulb, pen, colour palette swatches, mouse, coffee cup and floating social icons"></div>
  </section>
</body>
</html>
```